Halloway's Events

This is a brochure to promotoe our party, event planning, meeting, rooms and capabilities.

THE LANTERN ROOM
Halloway’s Party, Function, Meeting, & Event Venue
When you plan a business meeting, conference, social gathering or event at Halloway’s tavern and Grill, you can feel confident it will be successful as well as unforgettable.
First, our Restaurant itself offers a impressive, tastefully designed meeting space, plus a number of amenities that are attractive to both meeting planners and attendees. Second, our restaurant’s on-site Management and Chef staff is comprised of dedicated professionals who’ll make sure your event goes off without a hitch.
A Fabulous Florida Celtic Tavern and Grill
The location of a meeting can make or break it. That’s partly why Halloway’s has been so popular with individuals, meeting professionals and attendees. We are easily accessed by car, with ample onsite parking, and Free Garage parking. We are located within the Meridian Pines Plaza, boasting over 5,000 sq ft of Restaurant space for your next Party or event, including private function rooms, (The Lantern), with full AV capability, private bar, and seating for over 50 and standing capacity up to 80.
Corporate Meeting Facilities
At Halloway’s, we can accommodate groups ranging from 10 to 200 attendees. We offer 5,000 square feet of newly renovated, elegantly appointed Restaurant space with private Break out room available. Options include dinner or lunch service, boardroom, meeting space, full AV capabilities, appetizers, set menu’s, live music and additional entertainment options.We also offer outdoor space that offer the best South Florida has to offer.

Supportive Staff and Event Packages
At Halloway’s, our experienced on-property Management and Culinary staff will help every step of the way, including planning the most efficient use of meeting space, meals, receptions, entertainment, registration and audiovisual needs. When it’s time for a break from work, our staff can also help with group recreation opportunities and teambuilding exercises, such as a fun themed parties, karaoke, Trivia, or the event of your choosing.
A great place to start your meeting or event planning is by checking out the THE LANTERN ROOM meeting space on our web site, www.hpbtavern-example.com, our stop in and speak with one of management or culinary staff members, or simply call us on 1-561-482-6031.
We promise your event will be unforgettable!
We look forward to being in service to you - Cead Mile Failte (one hundred thousand welcomes)
Slainte!

Spec's TRI fold Brochure full color two sides from printa nova

Full Bleed Size (starting document size)

11.10" x 8.63"
282 x 219 mm
3331 x 2588 pixels

* Finished artwork should use the full bleed dimensions for best results.

Document Trim Size (final size after being cut)

10.98" x 8.50"
279 x 216 mm
3295 x 2551 pixels

* Please be sure to keep all text within the safe margin.

Resolution

300 DPI

* Dotted lines indicate where a fold will take place. If you don’t want copy or design to appear on the fold, make sure they stay within each panel’s safe margin.

Target Market(s)

Individuals, Comapanies, Meet up groups, and event planners.

Industry/Entity Type

Event Planning

Requirements
Must have
• Logo, description of our events, address and web site

2740 Larkspur Blvd., Suite 310
Harbor Vale, Florida 33499
PH:1-561-482-6031
email: hpbtavern@mailpost-example.com
web www.hpbtavern-example.com
FREE GARAGE PARKING
(Just east of Wexmoor in the Meridian Pines Plaza near Brewlark and the Cork Loft)
Hours of Operation
Sun-Thurs 11:30am - Midnight
Fri - Sat 11:30am - 2:00am
Nice to have
• FUN PHOTOS AND INCORPORATE FOOD WHERE POSSIBLE FESTIVE

```html
<!DOCTYPE html>
<html lang="en">
<head>
<meta charset="utf-8">
<title>Halloway's Events – Tri-fold Brochure, Outside</title>
<link rel="stylesheet" href="https://fonts.googleapis.com/css2?family=Cinzel:wght@700&family=Lato:wght@400;700&display=swap">
<style>
  :root{
    --backdrop:#e6e6e6;
    --brown-dark:#2e1f14;
    --brown:#46301f;
    --brown-light:#5a3e28;
    --charcoal:#222222;
    --charcoal-soft:#2d2d2d;
    --orange:#ec9a3c;
    --cream:#f2e6d2;
    --paper:#f4f4f2;
    --frame:#d9c7a6;
    --brand-green:#2f6a3a;
  }
  *{box-sizing:border-box;margin:0;padding:0}
  html,body{width:1200px;height:900px;overflow:hidden}
  body{background:var(--backdrop);font-family:"Lato",sans-serif;position:relative}
  address{font-style:normal}

  .brochure{
    position:absolute;left:45px;top:21px;width:1110px;height:858px;
    display:flex;box-shadow:0 6px 18px rgba(0,0,0,.18);
  }
  .panel{width:370px;height:100%;position:relative;overflow:hidden}

  /* Left panel */
  .panel--staff{background:linear-gradient(180deg,var(--brown-light),var(--brown) 45%,var(--brown-dark));color:var(--cream)}
  .staff-photo{
    position:absolute;left:0;top:0;width:100%;height:220px;
    background:linear-gradient(135deg,#c9a178,#8a5a3a 45%,#d8b98e 70%,#6e4a32);
    clip-path:polygon(0 0,100% 0,100% 78%,92% 84%,83% 80%,72% 88%,60% 83%,48% 90%,36% 85%,24% 92%,12% 86%,0 93%);
  }
  .staff-copy{position:absolute;left:30px;right:30px;top:228px}
  .staff-title{
    font-family:"Cinzel",serif;font-weight:700;color:var(--orange);
    font-size:19px;line-height:1.2;text-align:center;text-transform:uppercase;margin-bottom:12px;
  }
  .staff-text{font-size:11.2px;line-height:1.45;margin-bottom:9px}
  .call-label{color:var(--orange);font-size:18px;font-weight:700;text-align:center;margin-top:6px}
  .call-number{color:var(--orange);font-size:27px;font-weight:700;text-align:center;line-height:1.1;margin-bottom:8px}
  .staff-closing{font-size:11.2px;line-height:1.45;text-align:center}
  .snapshot{
    position:absolute;border:4px solid var(--frame);
    box-shadow:0 3px 8px rgba(0,0,0,.45);
  }
  .snapshot--dining{left:22px;top:690px;width:150px;height:110px;transform:rotate(-4deg);
    background:linear-gradient(135deg,#7a5440,#b98c6a 50%,#5d3d2c)}
  .snapshot--family{left:150px;top:705px;width:150px;height:112px;transform:rotate(5deg);
    background:linear-gradient(135deg,#3f5f7e,#c7a184 50%,#e6d3c0)}

  /* Middle panel */
  .panel--contact{background:radial-gradient(circle at 50% 50%,var(--charcoal-soft),var(--charcoal))}
  .dome{position:absolute;left:35px;width:300px;height:220px;overflow:hidden}
  .dome--room{top:55px;border-radius:0 0 150px 150px;
    background:linear-gradient(180deg,#6a4a30,#b88a5a 55%,#8a6040)}
  .dome--bar{bottom:55px;border-radius:150px 150px 0 0;
    background:linear-gradient(180deg,#4a5a3a,#c6a476 45%,#7a5a3c)}
  .contact-block{
    position:absolute;left:0;right:0;top:390px;text-align:center;
    color:var(--orange);font-size:13px;font-weight:700;line-height:1.45;
  }

  /* Right panel (cover) */
  .panel--cover{background:var(--paper)}
  .brand{position:absolute;left:0;right:0;top:62px;display:flex;justify-content:center;align-items:center;gap:10px}
  .brand-mark{width:30px;height:30px;background:var(--brand-green)}
  .brand-name{font-weight:700;font-size:22px;line-height:1.1;color:var(--brand-green)}
  .cover-photo{
    position:absolute;left:0;top:190px;width:100%;height:520px;
    background:linear-gradient(160deg,#5a2f22,#b5653f 35%,#d99a6b 55%,#7a3a2a 80%,#3e2419);
  }
  .cover-band{
    position:absolute;left:0;bottom:0;width:100%;height:150px;
    background:linear-gradient(180deg,rgba(70,48,31,.92),var(--brown-dark));
  }
  .call-tag{
    position:absolute;left:28px;top:-22px;padding:6px 20px 8px;
    background:linear-gradient(180deg,#b08a60,#7a5738);border-radius:10px;
    color:var(--cream);text-align:center;font-weight:700;
  }
  .call-tag .tag-label{font-size:17px;line-height:1.1}
  .call-tag .tag-number{font-size:21px;line-height:1.1}
  .cover-address{position:absolute;left:40px;top:58px;color:var(--orange);font-size:12.5px;font-weight:700;line-height:1.45}
</style>
</head>
<body>
<main class="brochure">

  <section class="panel panel--staff">
    <div class="staff-photo" role="img" aria-label="Photo of smiling guests posing together in the tavern"></div>
    <div class="staff-copy">
      <h2 class="staff-title">Supportive<br>Staff &amp; Event Packages</h2>
      <p class="staff-text">At Halloway’s, our experienced on-property Management and Culinary staff will help every step of the way, including planning the most efficient use of meeting space, meals, receptions, entertainment, registration and audiovisual needs. When it’s time for a break from work, our staff can also help with group recreation opportunities and teambuilding exercises, such as a fun themed parties, karaoke, Trivia, or the event of your choosing.</p>
      <p class="staff-text">To start your meeting or event planning is by checking out the The Lantern room meeting space on our web site www.hpbtavern-example.com, our stop in and speak with one of management or culinary staff members, or simply</p>
      <p class="call-label">call us on</p>
      <p class="call-number">1-561-482-6031.</p>
      <p class="staff-closing">We promise your event will be unforgettable! We look forward to being in service to you - Cead Mile Failte (one hundred thousand welcomes) Slainte!</p>
    </div>
    <div class="snapshot snapshot--dining" role="img" aria-label="Photo of guests dining at a table"></div>
    <div class="snapshot snapshot--family" role="img" aria-label="Photo of a guest holding a baby"></div>
  </section>

  <section class="panel panel--contact">
    <div class="dome dome--room" role="img" aria-label="Photo of the function room with framed pictures and wooden floor"></div>
    <address class="contact-block">
      www.hpbtavern-example.com<br>
      Harbor Vale, Florida 33499<br>
      PH:1-561-482-6031<br>
      Email: hpbtavern@mailpost-example.com
    </address>
    <div class="dome dome--bar" role="img" aria-label="Photo of the bartender pulling pints at the taps"></div>
  </section>

  <section class="panel panel--cover">
    <div class="brand">
      <span class="brand-mark"></span>
      <span class="brand-name">Halloway’s<br>Tavern &amp; Grill</span>
    </div>
    <div class="cover-photo" role="img" aria-label="Photo of a crowded, festive tavern dining room"></div>
    <div class="cover-band">
      <div class="call-tag">
        <div class="tag-label">call us on</div>
        <div class="tag-number">1-561-482-6031</div>
      </div>
      <address class="cover-address">
        Harbor Vale, Florida 33499<br>
        PH:1-561-482-6031<br>
        Email: hpbtavern@mailpost-example.com
      </address>
    </div>
  </section>

</main>
</body>
</html>
```